Diet product based by mushroom

My company name is HealtHomeIt means heal + home(healing & safe)Our target is women who are twenties - thirties having job & desire to lose weight within short terms about a week, two weeks, a monthMy company makes diet product based on mushrooms So we are looking for this packaging design of black mushroom + enoki mushroom. This product consists of one set(10 stick - each stick 3g) My company's main color is pastel yellow wish & white and company's mission is whoever we make relationship helps their life with mentally, physically We would like to see designs that use the color of our company logoThank you

Target Market(s)

Women who are twenties, thirties having job & desire to lose weight within short terms about a week, two weeks, a month

Colors
f6faec
eaf2ce
cadf82
abd036
9bcb3b

Requirements
Must have
• My project must have logo's color, the word (소라결, the food of gods')
• simple
Nice to have
• simple & highlight,legibility, simple&white
Should not have
• unbalance

```html
<!DOCTYPE html>
<html lang="ko">
<head>
<meta charset="utf-8">
<title>소라결 패키지 전면</title>
<link rel="stylesheet" href="https://fonts.googleapis.com/css2?family=Nanum+Gothic:wght@400;700&family=Nanum+Myeongjo:wght@700&display=swap">
<style>
  :root {
    --canvas: #e4e4e4;
    --panel: #ffffff;
    --brand-green: #4aa866;
    --title-ink: #3a3a3a;
    --tagline-ink: #555555;
    --lime-light: #eaf2ce;
    --lime-mid: #abd036;
    --lime-deep: #5cb81c;
  }
  * { margin: 0; padding: 0; box-sizing: border-box; }
  html, body {
    width: 1200px;
    height: 884px;
    overflow: hidden;
    background: var(--canvas);
  }
  .package-front {
    position: absolute;
    left: 377px;
    top: 32px;
    width: 446px;
    height: 820px;
    background: var(--panel);
    overflow: hidden;
  }
  .brand {
    position: absolute;
    top: 200px;
    left: 0;
    width: 100%;
    text-align: center;
  }
  .brand-name {
    font-family: "Nanum Gothic", sans-serif;
    font-weight: 400;
    font-size: 24px;
    letter-spacing: 3px;
    color: var(--brand-green);
  }
  .brand-tagline {
    margin-top: 4px;
    font-family: "Nanum Myeongjo", serif;
    font-weight: 700;
    font-size: 10px;
    color: var(--tagline-ink);
  }
  .product-title {
    position: absolute;
    top: 300px;
    left: 0;
    width: 100%;
    text-align: center;
    font-family: "Nanum Gothic", sans-serif;
    font-weight: 400;
    font-size: 62px;
    letter-spacing: 2px;
    color: var(--title-ink);
  }
  .fresh-wave-art {
    position: absolute;
    left: 0;
    bottom: 0;
    width: 100%;
    height: 390px;
    background: linear-gradient(to bottom,
      rgba(255,255,255,0) 0%,
      var(--lime-light) 18%,
      var(--lime-mid) 45%,
      var(--lime-deep) 100%);
  }
</style>
</head>
<body>
  <main class="package-front">
    <header class="brand">
      <p class="brand-name">BrivoNest</p>
      <p class="brand-tagline">가볍게 채우다, 소라결</p>
    </header>
    <h1 class="product-title">소라결</h1>
    <div class="fresh-wave-art" role="img" aria-label="연두색 빛망울과 흐르는 물결 선이 어우러진 상쾌한 그린 배경"></div>
  </main>
</body>
</html>
```